Storage Company Newsletter

We need a design for a newsletter for our company Vaultrix, a digital and physical asset storage company .The newsletter will be informative and educational covering tips on secure storage of personal documents and items both at home and at the work place. Rest easy with Vaultrix is our mantra. We have a pre-existing trademark & logo. Colors are blue and green. We can share the cmyk/rgb color information and background is grey.

Target Market(s)

Mass market – Middle to High income individuals

Industry/Entity Type

Digital

Font styles to use
Sans Serif

Colors
0393ce
00a88f
edf2f7

Requirements
Must have
• The newsletter linked to a CMS. In HTML5; Mail-chimp integration readable on Gmail, Yahoo, Hotmail and Outlook
Nice to have
• Sections of the newsletter are:
• Cover story
• News Flash
• Mwanachi Perspective
• Spotlight on the Counties
• CEO's Corner
• Tips and Helpful Information
• Important Dates and Events

```html
<!DOCTYPE html>
<html lang="en">
<head>
<meta charset="utf-8">
<title>Vaultrix Newsletter</title>
<link rel="stylesheet" href="https://fonts.googleapis.com/css2?family=Arimo:wght@400;700&display=swap">
<style>
  :root{
    --page-grey:#5f6a75;
    --paper:#ffffff;
    --blue:#3d92d5;
    --green:#00a88f;
    --ink:#2b2b2b;
    --body-ink:#444a50;
    --rule:#e6e9ec;
    --footer:#ebebeb;
    --black:#111111;
  }
  *{box-sizing:border-box;margin:0;padding:0}
  html,body{width:1200px;height:3504px;overflow:hidden;background:#fff}
  body{font-family:"Arimo",Arial,sans-serif;color:var(--ink);position:relative}
  .page-backdrop{position:absolute;left:0;top:0;width:1200px;height:3087px;background:var(--page-grey)}
  .newsletter{position:absolute;left:257px;top:0;width:715px;height:3028px;background:var(--paper)}
  .abs{position:absolute}
  .masthead{left:0;top:0;width:715px;height:257px;
    background:linear-gradient(160deg,#4a4d52 0%,#26282b 55%,#151617 100%)}
  .masthead-icon{left:335px;top:80px}
  .masthead-title{left:0;top:155px;width:715px;text-align:center;color:#fff;font-weight:700;font-size:28px;letter-spacing:1px}
  .story-title{color:var(--green);font-weight:700;font-size:20px;line-height:26px}
  .story-text{color:var(--body-ink);font-size:13.5px;line-height:21px}
  .btn{display:block;width:102px;height:30px;background:var(--blue);color:#fff;font-size:11px;font-weight:700;text-align:center;line-height:30px}
  .thumb{border-radius:0}
  .band{left:0;width:715px;background:var(--blue);color:#fff;font-size:21px;text-align:center;text-transform:uppercase}
  .divider{left:90px;width:535px;height:1px;background:var(--rule)}
  .byline{font-size:10px;color:var(--body-ink)}
  .byline b{color:var(--ink)}
  .text-link{color:var(--green);font-size:14px;font-weight:700}
  .signup-title{left:90px;top:2514px;padding-left:12px;border-left:5px solid var(--black);font-size:31px;line-height:33px;font-weight:700;color:var(--black);text-transform:uppercase;width:300px}
  .signup-input{left:406px;top:2511px;width:140px;height:41px;border:2px solid var(--black);font-size:11px;line-height:37px;padding-left:10px;color:var(--ink)}
  .signup-btn{left:546px;top:2511px;width:79px;height:41px;background:var(--black);color:#fff;font-size:12px;font-weight:700;text-align:center;line-height:41px}
  .footer{left:0;top:2783px;width:715px;height:245px;background:var(--footer)}
  .contact-heading{left:403px;top:58px;font-size:17px;font-weight:700;color:var(--black)}
  .contact-line{left:403px;font-size:12px;color:var(--body-ink)}
  .contact-line.email{color:var(--blue)}
  .social{left:242px;top:157px}
</style>
</head>
<body>
<div class="page-backdrop"></div>
<main class="newsletter">

  <header class="abs masthead" role="img" aria-label="Dark close-up photo of a laptop keyboard"></header>
  <svg class="abs masthead-icon" width="46" height="46" viewBox="0 0 46 46" aria-hidden="true">
    <circle cx="23" cy="23" r="21" fill="none" stroke="#fff" stroke-width="2"/>
    <rect x="15" y="16" width="16" height="14" rx="2" fill="none" stroke="#fff" stroke-width="2"/>
    <line x1="15" y1="21" x2="31" y2="21" stroke="#fff" stroke-width="2"/>
  </svg>
  <h1 class="abs masthead-title">SPOTLIGHT ON THE COUNTIES</h1>

  <!-- Spotlight story 1 -->
  <h2 class="abs story-title" style="left:90px;top:288px">Spotlight on the Counties # 1</h2>
  <p class="abs story-text" style="left:90px;top:326px;width:355px">Lorem ipsum dolor sit amet, consectetur adipiscing elit, sed do eiusmod tempor incididunt ut labore et dolore magna aliqua. Ut enim ad minim veniam. Duis aute irure dolor in.</p>
  <a class="abs btn" style="left:90px;top:435px">Read more</a>
  <div class="abs thumb" style="left:458px;top:292px;width:126px;height:126px;background:linear-gradient(135deg,#d9c27a,#7a8a3e 55%,#3c4a2a)" role="img" aria-label="Photo of a market stall with fresh produce"></div>

  <!-- Spotlight story 2 -->
  <div class="abs thumb" style="left:90px;top:511px;width:167px;height:126px;background:linear-gradient(160deg,#c77a9a,#6c4a7e 50%,#2e2440)" role="img" aria-label="Photo of a steel bridge at sunset"></div>
  <h2 class="abs story-title" style="left:283px;top:505px">Spotlight on the Counties # 2</h2>
  <p class="abs story-text" style="left:283px;top:541px;width:345px">Lorem ipsum dolor sit amet, consectetur adipiscing elit, sed do eiusmod tempor incididunt ut labore et dolore magna aliqua. Ut enim ad minim veniam. Duis aute irure dolor in reprehenderit.</p>
  <a class="abs btn" style="left:283px;top:654px">Read more</a>

  <!-- Mwanachi Perspective -->
  <div class="abs band" style="top:736px;height:87px;line-height:87px">Mwanachi Perspective</div>
  <h2 class="abs story-title" style="left:90px;top:846px">Mwanachi Perspective</h2>
  <p class="abs story-text" style="left:90px;top:880px;width:535px">Lorem ipsum dolor sit amet, consectetur adipiscing elit, sed do eiusmod tempor incididunt ut labore et dolore magna aliqua. Ut enim ad minim veniam, quis nostrud exercitation ullamco laboris nisi ut aliquip ex ea commodo consequat. Duis aute irure dolor in reprehenderit in voluptate velit esse cillum dolore eu fugiat nulla pariatur. Excepteur sint occaecat cupidatat non proident, sunt in culpa qui officia deserunt mollit anim id est laborum. Sed ut perspiciatis unde omnis iste natus...</p>
  <a class="abs btn" style="left:90px;top:1037px">Read more</a>

  <h2 class="abs story-title" style="left:90px;top:1109px">Mwanachi Perspective</h2>
  <p class="abs story-text" style="left:90px;top:1143px;width:535px">Lorem ipsum dolor sit amet, consectetur adipiscing elit, sed do eiusmod tempor incididunt ut labore et dolore magna aliqua. Ut enim ad minim veniam, quis nostrud exercitation ullamco laboris nisi ut aliquip ex ea commodo consequat. Duis aute irure dolor in reprehenderit in voluptate velit esse cillum dolore eu fugiat nulla pariatur. Excepteur sint occaecat cupidatat non proident, sunt in culpa qui officia deserunt mollit anim id est laborum. Sed ut perspiciatis unde omnis iste natus...</p>
  <a class="abs btn" style="left:90px;top:1302px">Read more</a>

  <!-- Important Dates and Events -->
  <div class="abs band" style="top:1358px;height:90px;line-height:90px">Important Dates and Events</div>
  <h2 class="abs story-title" style="left:90px;top:1465px;width:266px;text-align:center">Important Dates and Events # 1</h2>
  <p class="abs story-text" style="left:90px;top:1520px;width:266px">Maecenas faucibus mollis interdum. Morbi leo risus, porta ac consectetur ac, vestibulum at eros. Aenean eu leo quam. Pellentesque ornare sem lacinia quam venenatis vestibulum.</p>
  <a class="abs btn" style="left:90px;top:1656px">Read more</a>

  <h2 class="abs story-title" style="left:382px;top:1465px;width:243px;text-align:center">Important Dates and Events # 2</h2>
  <p class="abs story-text" style="left:382px;top:1520px;width:243px">Maecenas faucibus mollis interdum. Morbi leo risus, porta ac consectetur ac, vestibulum at eros. Aenean eu leo quam. Pellentesque ornare sem lacinia quam venenatis vestibulum.</p>
  <a class="abs btn" style="left:382px;top:1656px">Read more</a>

  <div class="abs divider" style="top:1732px"></div>

  <!-- CEO's Corner -->
  <div class="abs" style="left:90px;top:1784px;width:535px;height:353px;background:linear-gradient(90deg,#c9ccd0,#eef0f2 40%,#d7d9dc 70%,#b9bdc2)" role="img" aria-label="Photo of the chief executive standing in an office archive"></div>
  <h2 class="abs story-title" style="left:90px;top:2160px">CEO's Corner</h2>
  <p class="abs byline" style="left:90px;top:2191px">Written by <b>CEO of Vaultrix</b> / February 2 2014</p>
  <p class="abs story-text" style="left:90px;top:2222px;width:535px">Lorem ipsum dolor sit amet, consectetur adipiscing elit, sed do eiusmod tempor incididunt ut labore et dolore magna aliqua. Ut enim ad minim veniam, quis nostrud exercitation ullamco laboris nisi ut aliquip ex ea commodo consequat. Duis aute irure dolor in reprehenderit in voluptate velit esse cillum dolore eu fugiat nulla pariatur. Excepteur sint occaecat cupidatat non proident, sunt in culpa qui officia deserunt...</p>
  <a class="abs text-link" style="left:90px;top:2332px">Read more</a>

  <div class="abs divider" style="top:2403px"></div>

  <!-- Newsletter signup -->
  <h2 class="abs signup-title">Sign up for our newsletter</h2>
  <div class="abs signup-input">Enter your Email</div>
  <div class="abs signup-btn">SIGN UP!</div>
  <p class="abs story-text" style="left:90px;top:2612px;width:535px">Lorem ipsum dolor sit amet, consectetur adipiscing elit, sed do eiusmod tempor incididunt ut labore et dolore magna aliqua. Ut enim ad minim veniam.</p>
  <a class="abs text-link" style="left:90px;top:2668px;font-weight:400;font-size:13px">Unsubscribe</a>

  <!-- Footer -->
  <footer class="abs footer">
    <h3 class="abs contact-heading">Contact</h3>
    <p class="abs contact-line" style="top:95px">+254700555012</p>
    <p class="abs contact-line email" style="top:117px">hello@vaultrix-mail.com</p>
    <svg class="abs social" width="230" height="30" viewBox="0 0 230 30" aria-hidden="true">
      <g fill="none" stroke="var(--blue)" stroke-width="1.5">
        <circle cx="14" cy="15" r="13"/>
        <circle cx="64" cy="15" r="13"/>
        <circle cx="116" cy="15" r="13"/>
        <circle cx="168" cy="15" r="13"/>
        <circle cx="218" cy="15" r="13"/>
      </g>
    </svg>
  </footer>
</main>
</body>
</html>
```